Hensby Estates Website and Logo Design

We need a new logo and website designed for 'Hensby Estates Ltd', which is a well established Guernsey property holding company founded in 1934.

The company does not currently have a website. The new website should be similar in style and layout to https://www.corvanhale.org/.

Target Market(s)

Industry, Media, Tenants

Industry/Entity Type

Property Management

Logo Text

HEL OR Hensby Estates Ltd OR HE

Coding

Coded - Design and coding required

Number of Pages Required

4 page

Font styles to use
Other font styles liked:
• Helvetica

Requirements
Must have
• The logo laying over the picture (like https://www.corvanhale.org/).
• Big pictures on homepage (like https://www.corvanhale.org/)

```html
<!DOCTYPE html>
<html lang="en">
<head>
<meta charset="utf-8">
<title>Hensby Estates Limited</title>
<link rel="stylesheet" href="https://fonts.googleapis.com/css2?family=Oswald:wght@400;500&family=Montserrat:wght@400;600;700&family=Open+Sans:wght@400;600&family=Merriweather:ital@1&display=swap">
<style>
:root{
  --green:#67b843;
  --green-dark:#55a133;
  --green-soft:#d9efcc;
  --ink:#1f1f1f;
  --body:#555;
  --muted:#8c8c8c;
  --line:#e4e4e4;
  --paper:#ffffff;
  --mist:#f8faf6;
  --stat-bg:#f5f5f5;
  --night:#1b2330;
}
*{margin:0;padding:0;box-sizing:border-box}
html,body{width:1200px;height:2922px;overflow:hidden;background:var(--paper)}
body{font-family:"Open Sans",Helvetica,Arial,sans-serif;color:var(--body);position:relative}
section,header,footer{position:absolute;left:0;width:1200px}
.abs{position:absolute}
.heading{font-family:Oswald,"Arial Narrow",sans-serif;font-weight:500;color:var(--ink);text-transform:uppercase;letter-spacing:.5px}

/* hero */
.hero{top:0;height:612px;background:linear-gradient(180deg,#1c2433 0%,#3b4a55 30%,#304b55 52%,#1d3a45 75%,#152a33 100%)}
.hero-photo{position:absolute;inset:0}
.brand{left:98px;top:18px;display:flex;align-items:center;gap:12px}
.brand-mark{width:40px;height:40px;background:var(--green)}
.brand-name{font-family:Montserrat,Helvetica,sans-serif;font-weight:700;font-size:22px;color:#fff;letter-spacing:1px}
.main-nav{right:98px;top:33px;display:flex;gap:43px}
.main-nav a{font-family:Montserrat,Helvetica,sans-serif;font-size:14px;color:#fff;text-decoration:none;text-transform:uppercase}
.nav-rule{left:480px;right:98px;top:88px;height:1px;background:rgba(255,255,255,.25)}
.hero-title{top:222px;width:1200px;text-align:center;font-family:Montserrat,Helvetica,sans-serif;font-weight:700;font-size:50px;color:#fff}
.hero-rule{left:408px;width:422px;top:300px;height:2px;background:#fff}
.hero-text{top:322px;width:1200px;text-align:center;font-family:Montserrat,Helvetica,sans-serif;font-size:17px;line-height:29px;color:#fff}
.btn{display:inline-flex;align-items:center;justify-content:center;font-family:Montserrat,Helvetica,sans-serif;font-weight:600;text-transform:uppercase;text-decoration:none;color:#fff;border-radius:3px}
.btn-solid{background:var(--green)}
.btn-ghost{border:2px solid var(--green);background:rgba(0,0,0,.15)}
.btn-line{border:2px solid #fff}
.hero .btn{top:420px;height:41px;font-size:14px}
.slide-arrow{top:318px}

/* welcome */
.welcome{top:612px;height:400px}
.kicker{left:98px;top:60px;font-family:Merriweather,Georgia,serif;font-style:italic;font-size:14px;color:var(--green)}
.welcome .heading{left:98px;top:82px;font-size:34px}
.welcome-text{left:98px;top:148px;width:472px;font-size:12.4px;line-height:22px;color:#444}
.welcome .btn{left:98px;top:300px;width:114px;height:37px;font-size:12px}
.video{left:625px;top:64px;width:477px;height:275px;background:linear-gradient(180deg,#5f79a8 0%,#8aa0c2 45%,#b8b4a6 70%,#3f5666 100%)}
.video svg{position:absolute;left:0;top:0}
.video-label{left:20px;top:246px;font-size:13px;color:#fff}

/* stats */
.stats{top:1015px;left:98px;width:1004px;height:111px;background:var(--stat-bg);display:flex;z-index:2}
.stat{flex:1;padding:6px 0 0 50px;border-left:1px solid var(--line)}
.stat:first-child{border-left:0}
.stat-num{font-family:Oswald,sans-serif;font-size:54px;line-height:64px;color:var(--green)}
.stat-label{font-family:Merriweather,Georgia,serif;font-style:italic;font-size:15px;color:#333}

/* location */
.location{top:1099px;height:395px}
.map{left:0;top:0;width:600px;height:395px;background:linear-gradient(135deg,#efece6 0%,#e7e4dc 60%,#ece6e9 100%)}
.location-panel{left:600px;top:0;width:600px;height:395px;background:linear-gradient(180deg,#2a2f37 0%,#1c1f25 100%);text-align:center;color:#fff}
.location-panel .heading{color:#fff;font-size:30px;position:absolute;top:152px;width:600px}
.location-text{position:absolute;top:205px;left:90px;width:420px;font-size:12.5px;line-height:25px}
.location-panel .btn{position:absolute;left:218px;top:279px;width:165px;height:38px;font-size:12px}

/* services */
.services{top:1494px;height:431px;text-align:center}
.section-title{width:1200px;font-size:32px}
.services .section-title{top:54px}
.subtitle{top:112px;width:1200px;font-family:Merriweather,Georgia,serif;font-style:italic;font-size:13.5px;color:#a6a6a6}
.service{top:160px;width:240px;text-align:center}
.service-icon{width:122px;height:122px;margin:0 auto}
.service h3{margin-top:22px;font-size:17px;font-weight:400}
.service h3.active{color:var(--green)}
.service p{margin-top:8px;font-size:12.5px;line-height:21px;color:var(--muted)}

/* news */
.news{top:1925px;height:385px;background:var(--mist)}
.news .section-title{top:60px;text-align:center}
.news-card{top:140px;width:477px;height:179px;background:#fff;display:flex}
.news-photo{width:204px;height:179px;flex:none}
.news-body{padding:14px 18px 0 20px}
.news-meta{display:flex;gap:34px;font-size:12px;color:#333;align-items:center}
.news-meta span{display:flex;align-items:center;gap:8px}
.news-body h4{margin-top:10px;font-family:Oswald,sans-serif;font-weight:400;font-size:16.5px;line-height:25px;color:var(--ink)}
.news-body p{margin-top:8px;font-size:12.2px;line-height:21px;color:#444;text-align:justify}

/* showing */
.showing{top:2310px;height:314px;background:linear-gradient(180deg,#6cbf45 0%,#62b43d 100%);text-align:center;color:#fff}
.showing .heading{color:#fff;top:62px;width:1200px;font-size:36px}
.showing-text{top:118px;left:300px;width:600px;font-size:14px;line-height:26px}
.showing .btn{top:207px;left:517px;width:166px;height:38px;font-size:12px}

/* footer */
.site-footer{top:2624px;height:298px}
.footer-col{top:50px}
.footer-col h5{font-family:Montserrat,Helvetica,sans-serif;font-weight:600;font-size:16px;color:var(--ink);text-transform:uppercase;margin-bottom:12px}
.footer-col a{display:block;font-size:13px;line-height:25.5px;color:#333;text-decoration:none}
.newsletter-note{font-size:12px;color:#333;text-transform:uppercase}
.signup{margin-top:12px;display:flex;width:251px;height:35px}
.signup-input{flex:1;border:1px solid #ccc;font-family:"Open Sans",sans-serif;font-style:italic;font-size:11px;color:#999;padding-left:12px;display:flex;align-items:center}
.signup-btn{width:43px;background:var(--green);display:flex;align-items:center;justify-content:center}
.footer-rule{left:98px;width:1004px;top:236px;height:1px;background:var(--line)}
.copyright{top:258px;width:1200px;text-align:center;font-size:12px;color:#555}
</style>
</head>
<body>

<header class="hero">
  <div class="hero-photo" role="img" aria-label="Harbour town with moored boats and waterfront houses at dusk"></div>
  <div class="abs brand"><span class="brand-mark"></span><span class="brand-name">HENSBY ESTATES</span></div>
  <nav class="abs main-nav">
    <a href="#">Home</a><a href="#">About Us</a><a href="#">Property Details</a><a href="#">Blog</a><a href="#">Gallery</a><a href="#">Contact Us</a>
  </nav>
  <div class="abs nav-rule"></div>
  <svg class="abs slide-arrow" style="left:44px" width="30" height="70" viewBox="0 0 30 70"><path d="M26 2 4 35l22 33" fill="none" stroke="#fff" stroke-width="2"/></svg>
  <svg class="abs slide-arrow" style="left:1126px" width="30" height="70" viewBox="0 0 30 70"><path d="M4 2l22 33L4 68" fill="none" stroke="#fff" stroke-width="2"/></svg>
  <h1 class="abs hero-title">HENSBY ESTATES LIMITED</h1>
  <div class="abs hero-rule"></div>
  <p class="abs hero-text">Hensby Estates Limited (HEL) is a family-owned Guernsey property holding<br>company. It purchases properties that are considered</p>
  <a class="abs btn btn-solid" href="#" style="left:405px;width:164px">Get More Info</a>
  <a class="abs btn btn-ghost" href="#" style="left:595px;width:201px">Schedule a Showing</a>
</header>

<section class="welcome">
  <p class="abs kicker">Hensby Estates Limited</p>
  <h2 class="abs heading">Welcome to Hensby Estates</h2>
  <p class="abs welcome-text">Hensby Estates Limited (HEL) is a family-owned Guernsey property holding company. It purchases properties that are considered to have potential for development either through refurbishment or by obtaining planning permission to change its classification from, for example, industrial premises to offices or retail outlets, or by the marriage value of buying an adjacent property to one already owned by HEL.</p>
  <a class="abs btn btn-solid" href="#">Read More</a>
  <div class="abs video" role="img" aria-label="Harbour with fishing boats and hillside town under a blue sky">
    <svg width="477" height="275" viewBox="0 0 477 275">
      <path d="M0 0 130 275H0Z" fill="#67b843" fill-opacity=".85"/>
      <circle cx="38" cy="210" r="17" fill="none" stroke="#fff" stroke-width="2"/>
      <path d="M33 201l14 9-14 9z" fill="#fff"/>
    </svg>
    <span class="abs video-label">Our Videos</span>
  </div>
</section>

<div class="abs stats">
  <div class="stat"><div class="stat-num">136</div><div class="stat-label">Good Property</div></div>
  <div class="stat"><div class="stat-num">355</div><div class="stat-label">Team Members</div></div>
  <div class="stat"><div class="stat-num">325</div><div class="stat-label">Square Areas</div></div>
  <div class="stat"><div class="stat-num">1225</div><div class="stat-label">Happy Customers</div></div>
</div>

<section class="location">
  <div class="abs map" role="img" aria-label="Street map of the parish around the property with a location marker"></div>
  <div class="abs location-panel">
    <svg class="abs" style="left:270px;top:78px" width="60" height="60" viewBox="0 0 60 60">
      <circle cx="30" cy="30" r="28" fill="none" stroke="#fff" stroke-width="3"/>
      <path d="M30 14c-7 0-12 5-12 12 0 9 12 20 12 20s12-11 12-20c0-7-5-12-12-12z" fill="#fff"/>
      <circle cx="30" cy="26" r="4.5" fill="#1f232a"/>
    </svg>
    <h2 class="heading">Property Location</h2>
    <p class="location-text">It is a long established fact that a reader will be distracted by the readable content of a page when looking at its layout.</p>
    <a class="btn btn-line" href="#">View in Large Map</a>
  </div>
</section>

<section class="services">
  <h2 class="abs heading section-title">Our Services</h2>
  <p class="abs subtitle">Marbrook Consulting is proud to offer various services</p>

  <div class="abs service" style="left:79px">
    <svg class="service-icon" viewBox="0 0 122 122"><circle cx="61" cy="61" r="59" fill="none" stroke="#444" stroke-width="3"/><circle cx="61" cy="61" r="52" fill="#8c8c8c"/><circle cx="61" cy="55" r="14" fill="none" stroke="#fff" stroke-width="3"/><path d="M55 55l4 4 8-8" fill="none" stroke="#fff" stroke-width="3"/><path d="M52 67l-5 17 9-4 5 7 0-15M70 67l5 17-9-4-5 7" fill="none" stroke="#fff" stroke-width="2.5"/></svg>
    <h3 class="heading">Best Quality</h3>
    <p>We are a team of experienced in home buyers renovators team</p>
  </div>
  <div class="abs service" style="left:346px">
    <svg class="service-icon" viewBox="0 0 122 122"><circle cx="61" cy="61" r="59" fill="none" stroke="#67b843" stroke-width="3"/><circle cx="61" cy="61" r="52" fill="#d9efcc"/><circle cx="61" cy="61" r="20" fill="none" stroke="#67b843" stroke-width="9"/><circle cx="61" cy="61" r="20" fill="none" stroke="#fff" stroke-width="9" stroke-dasharray="10 21.4"/></svg>
    <h3 class="heading active">Ensure Their Safety</h3>
    <p>We are a team of experienced in home buyers renovators team</p>
  </div>
  <div class="abs service" style="left:612px">
    <svg class="service-icon" viewBox="0 0 122 122"><circle cx="61" cy="61" r="59" fill="none" stroke="#444" stroke-width="3"/><circle cx="61" cy="61" r="52" fill="#8c8c8c"/><circle cx="50" cy="50" r="8" fill="#fff"/><circle cx="72" cy="50" r="8" fill="#fff"/><path d="M36 78c0-12 7-18 14-18s14 6 14 18zM58 78c0-12 7-18 14-18s14 6 14 18z" fill="#fff"/></svg>
    <h3 class="heading">Welcomes Family Members</h3>
    <p>We are a team of experienced in home buyers renovators team</p>
  </div>
  <div class="abs service" style="left:879px">
    <svg class="service-icon" viewBox="0 0 122 122"><circle cx="61" cy="61" r="59" fill="none" stroke="#444" stroke-width="3"/><circle cx="61" cy="61" r="52" fill="#8c8c8c"/><circle cx="54" cy="54" r="9" fill="#fff"/><path d="M38 80c0-11 7-16 16-16s16 5 16 16z" fill="#fff"/><circle cx="76" cy="58" r="9" fill="none" stroke="#fff" stroke-width="4" stroke-dasharray="4 3"/></svg>
    <h3 class="heading">Day to Day Administration</h3>
    <p>We are a team of experienced in home buyers renovators team</p>
  </div>
</section>

<section class="news">
  <h2 class="abs heading section-title">Our Latest News</h2>
  <article class="abs news-card" style="left:98px">
    <div class="news-photo" role="img" aria-label="Bay with moored boats and a headland" style="background:linear-gradient(180deg,#7f9cc4 0%,#a9bcd6 40%,#3f6f7f 62%,#2f5a66 100%)"></div>
    <div class="news-body">
      <div class="news-meta"><span><svg width="10" height="10" viewBox="0 0 10 10"><circle cx="5" cy="3" r="2.5" fill="#67b843"/><path d="M0 10c0-4 2-5 5-5s5 1 5 5z" fill="#67b843"/></svg>John Doe</span><span><svg width="11" height="10" viewBox="0 0 11 10"><rect x=".5" y="1.5" width="10" height="8" fill="none" stroke="#67b843"/><rect x=".5" y="1.5" width="10" height="2.5" fill="#67b843"/></svg>30/04/2016</span></div>
      <h4>Edwin Hensby to manage both his own extensive Investments</h4>
      <p>Many Guernsey-registered companies have a policy of renting property rather than pur chasing. Most prefer to put their capital</p>
    </div>
  </article>
  <article class="abs news-card" style="left:625px">
    <div class="news-photo" role="img" aria-label="Harbour with small boats and a rocky shore" style="background:linear-gradient(180deg,#5d86c9 0%,#9fb8dd 45%,#4b7890 62%,#5d6a5c 100%)"></div>
    <div class="news-body">
      <div class="news-meta"><span><svg width="10" height="10" viewBox="0 0 10 10"><circle cx="5" cy="3" r="2.5" fill="#67b843"/><path d="M0 10c0-4 2-5 5-5s5 1 5 5z" fill="#67b843"/></svg>John Doe</span><span><svg width="11" height="10" viewBox="0 0 11 10"><rect x=".5" y="1.5" width="10" height="8" fill="none" stroke="#67b843"/><rect x=".5" y="1.5" width="10" height="2.5" fill="#67b843"/></svg>30/04/2016</span></div>
      <h4>Edwin Hensby to manage both his own extensive Investments</h4>
      <p>Many Guernsey-registered companies have a policy of renting property rather than pur chasing. Most prefer to put their capital</p>
    </div>
  </article>
</section>

<section class="showing" role="img" aria-label="Green tinted harbour view behind the call to action">
  <h2 class="abs heading">Interested &nbsp;in a Showing?</h2>
  <p class="abs showing-text">Despite the somewhat glorified title of Governing Director General of the company, Edwin Hensby ensured that he, together with his six children</p>
  <a class="abs btn btn-line" href="#">Schedule a Show</a>
</section>

<footer class="site-footer">
  <div class="abs footer-col" style="left:98px"><h5>Company</h5><a href="#">About us</a><a href="#">Protfolio</a><a href="#">Gallery</a><a href="#">Conatct us</a></div>
  <div class="abs footer-col" style="left:308px"><h5>Property Areas</h5><a href="#">Bailiwick of Guernsey</a><a href="#">Tenants personally</a><a href="#">Ensure their safety</a><a href="#">Streamline your supply chain.</a></div>
  <div class="abs footer-col" style="left:588px"><h5>Why Guernsey?</h5><a href="#">The Bailiwick of Guernsey</a><a href="#">British Crown</a><a href="#">Ideal financial</a><a href="#">Guernsey-registered</a></div>
  <div class="abs footer-col" style="left:851px"><h5>Newsletter</h5>
    <p class="newsletter-note">Sign up for a free week!</p>
    <div class="signup"><span class="signup-input">Enter Your Mail Id</span><span class="signup-btn"><svg width="16" height="16" viewBox="0 0 16 16"><path d="M1 7 15 1 11 15 8 9z" fill="#fff"/></svg></span></div>
  </div>
  <div class="abs footer-rule"></div>
  <p class="abs copyright">Copyrights@CompanyName , All rights Reserved</p>
</footer>

</body>
</html>
```